Clear Meadow Cleaning Services - New Brochure Design Project

Need a very good and polished Brochure from my Commercial Cleaning Services business. I have attached what I have done in the past. Need to take to the next level . Something that will compliment my website .https://quentin-v.sitenook.example/

Target Market(s)

Business /Schools/Churches/ Just about any non-residential establishment

Requirements
Must have
• Professional / Polished look and feel

```html
<!DOCTYPE html>
<html lang="en">
<head>
<meta charset="utf-8">
<title>Clear Meadow Cleaning Services – Trifold Brochure</title>
<link href="https://fonts.googleapis.com/css2?family=Source+Sans+3:ital,wght@0,400;0,600;0,700;1,400&family=Roboto+Condensed:wght@700&display=swap" rel="stylesheet">
<style>
:root{
  --navy:#1f3c8c;
  --navy-deep:#162c6e;
  --green:#8cc63f;
  --sky:#29a9e0;
  --ink:#3b3b3b;
  --muted:#6b6b6b;
  --paper:#ffffff;
  --stage:#e6e6e8;
}
*{box-sizing:border-box;margin:0;padding:0}
html,body{width:826px;height:1200px;overflow:hidden;background:var(--stage)}
body{position:relative;font-family:"Source Sans 3",Arial,sans-serif;color:var(--ink)}
.sheet{position:absolute;left:76px;width:666px;height:517px;background:var(--paper);box-shadow:0 12px 14px -8px rgba(0,0,0,.35);overflow:hidden}
.sheet--outside{top:57px}
.sheet--inside{top:627px}
.panel{position:absolute;top:0;height:100%;overflow:hidden}
.abs{position:absolute}
.photo{position:absolute}
.navy-bg{background:linear-gradient(180deg,#2a4fa6 0%,var(--navy) 45%,var(--navy-deep) 100%)}
.phone-btn{position:absolute;height:23px;border-radius:12px;background:var(--green);color:#fff;font-weight:600;font-size:16px;letter-spacing:.8px;display:flex;align-items:center;justify-content:center;gap:6px;box-shadow:0 2px 3px rgba(0,0,0,.25)}
.phone-btn svg{width:14px;height:14px}
.brand-mark{display:flex;align-items:center;gap:6px}
.brand-dot{width:22px;height:22px;border-radius:50%;background:var(--sky);flex:none}
.brand-name{font-weight:600;color:var(--green);font-size:15px;line-height:1.1;text-align:center}
.tagline{color:var(--green);font-size:12.5px;text-align:center;width:100%}
/* services list */
.service{position:absolute;left:12px;display:flex;gap:8px}
.service-icon{width:32px;height:32px;border-radius:50%;background:radial-gradient(circle at 40% 35%,#5cc4f0,var(--sky));box-shadow:0 0 0 3px #e3eef6;flex:none}
.service h4{font-size:8px;font-weight:700;color:var(--navy);margin-top:2px}
.service p{font-size:6.6px;line-height:7.6px;color:var(--muted)}
.checklist li{list-style:none;display:flex;align-items:center;gap:8px;color:#fff;font-size:8.6px;height:23px;border-bottom:1px dotted rgba(255,255,255,.45)}
.tick{width:10px;height:10px;border:1px solid #fff;border-radius:50%;flex:none;position:relative}
.tick::after{content:"";position:absolute;left:2.5px;top:1px;width:3px;height:5px;border:solid #fff;border-width:0 1px 1px 0;transform:rotate(45deg)}
.offer-list li{list-style:none;font-size:9.5px;color:var(--muted);height:17.5px;display:flex;align-items:center;gap:5px}
.offer-list li::before{content:"";width:6px;height:6px;border:1px solid var(--green);border-radius:50%}
</style>
</head>
<body>

<!-- Outside spread -->
<section class="sheet sheet--outside">

  <!-- Services panel -->
  <div class="panel" style="left:0;width:217px;background:#fff">
    <div class="photo" role="img" aria-label="Photo of two cleaners wiping desks and a whiteboard in a bright office" style="left:0;top:0;width:217px;height:245px;background:linear-gradient(160deg,#eef1f4 0%,#d4dbe2 55%,#bcc6cf 100%)"></div>
    <svg class="abs" style="left:0;top:200px" width="217" height="60" viewBox="0 0 217 60" preserveAspectRatio="none">
      <path d="M0 20 Q110 50 217 6 L217 60 L0 60Z" fill="#fff"/>
      <path d="M0 14 Q110 46 217 0 L217 6 Q110 52 0 22Z" fill="var(--green)"/>
    </svg>
    <div class="abs" style="left:0;top:235px;width:155px;height:26px;background:var(--green);border-radius:0 13px 13px 0;color:#fff;font-size:13px;padding:5px 12px;letter-spacing:.3px">SERVICES</div>
    <div class="service" style="top:277px"><span class="service-icon"></span><div><h4>COMMERCIAL</h4><p>• Office cleaning<br>• Event Cleaning Services<br>• Malls</p></div></div>
    <div class="service" style="top:322px"><span class="service-icon"></span><div><h4>FACILITY</h4><p>• Multi-Tenant Office Buildings<br>• Single-Tenant Buildings<br>• Owner-Occupied Buildings</p></div></div>
    <div class="service" style="top:370px"><span class="service-icon"></span><div><h4>HEALTHCARE</h4><p>• Hospitals &amp; Treatment Centres<br>• Health Clinics<br>• Senior Living &amp; Long-Term Care</p></div></div>
    <div class="service" style="top:415px"><span class="service-icon"></span><div><h4>EDUCATIONAL</h4><p>• School Boards (K-12)<br>• Post-Secondary (University, College, Vocational)</p></div></div>
    <div class="service" style="top:458px"><span class="service-icon"></span><div><h4>INDUSTRIAL</h4><p>• Factories<br>• Warehouses<br>• Distribution Centres</p></div></div>
  </div>

  <!-- Contact panel -->
  <div class="panel navy-bg" style="left:217px;width:219px">
    <div class="photo" role="img" aria-label="Round photo of a cleaner mopping a glossy office floor" style="left:43px;top:19px;width:132px;height:132px;border-radius:50%;border:3px solid #fff;background:radial-gradient(circle at 50% 40%,#e9eef2,#b8c5d0)"></div>
    <div class="abs brand-mark" style="left:0;top:200px;width:219px;flex-direction:column">
      <span class="brand-name">Clear Meadow<br>Cleaning Services</span>
      <span class="brand-dot" style="width:30px;height:30px"></span>
    </div>
    <div class="abs tagline" style="top:281px">We Enjoy Doing The Dirty work</div>
    <h3 class="abs" style="top:302px;width:100%;text-align:center;color:#fff;font-size:12px;font-weight:600">CONTACT US</h3>
    <p class="abs" style="top:320px;left:15px;width:189px;text-align:center;color:#fff;font-size:9.4px;line-height:13.3px">We are a full service cleaning company that offers a full range of quality cleaning services to fit your needs no matter the size. We offer commercial and residential cleaning services to fit any size property. We take pride in doing your dirty work.</p>
    <div class="phone-btn" style="left:19px;top:412px;width:180px">
      <svg viewBox="0 0 16 16"><circle cx="8" cy="8" r="7" fill="none" stroke="#fff" stroke-width="1.4"/><path d="M5.5 4.5l1.5 1.6-.7 1c.5 1 1.3 1.8 2.3 2.3l1-.7 1.6 1.5-.9 1.1C8.4 11 5 7.6 4.4 5.4z" fill="#fff"/></svg>(302) 555-0148</div>
    <div class="abs" style="top:451px;left:76px;display:flex;gap:13px">
      <span style="width:14px;height:14px;border:1px solid var(--green);border-radius:50%"></span>
      <span style="width:14px;height:14px;border:1px solid var(--green);border-radius:50%"></span>
      <span style="width:14px;height:14px;border:1px solid var(--green);border-radius:50%"></span>
      <span style="width:14px;height:14px;border:1px solid var(--green);border-radius:50%"></span>
    </div>
    <div class="abs" style="top:484px;width:100%;text-align:center;color:#fff;font-weight:700;font-size:11.5px">www.quentin-v.sitenook.example</div>
  </div>

  <!-- Cover panel -->
  <div class="panel" style="left:436px;width:230px;background:#fff">
    <div class="abs brand-mark" style="left:12px;top:22px">
      <span class="brand-dot" style="width:28px;height:28px"></span>
      <div>
        <div style="color:var(--navy);font-size:18px;line-height:19px;font-weight:600">Clear Meadow<br>Cleaning Services</div>
        <div style="color:var(--green);font-size:9.5px;margin-top:3px">We enjoy doing the dirty work</div>
      </div>
    </div>
    <div class="photo" role="img" aria-label="Photo of a bright modern office with a long black desk and pendant lights" style="left:0;top:130px;width:230px;height:272px;background:linear-gradient(180deg,#f3f4f5 0%,#d8dcdf 50%,#a9aeb2 100%)"></div>
    <svg class="abs" style="left:0;top:95px" width="230" height="75" viewBox="0 0 230 75" preserveAspectRatio="none">
      <path d="M0 0 L230 0 L230 14 Q120 62 0 40Z" fill="#fff"/>
      <path d="M0 36 Q120 58 230 10 L230 20 Q120 70 0 48Z" fill="var(--navy)"/>
      <path d="M0 46 Q120 68 230 18 L230 24 Q120 76 0 54Z" fill="var(--green)"/>
    </svg>
    <svg class="abs" style="left:0;top:380px" width="230" height="30" viewBox="0 0 230 30" preserveAspectRatio="none">
      <path d="M0 14 Q120 30 230 0 L230 30 L0 30Z" fill="#fff"/>
      <path d="M0 10 Q120 26 230 -4 L230 0 Q120 32 0 16Z" fill="var(--sky)"/>
    </svg>
    <h2 class="abs" style="top:427px;width:100%;text-align:center;font-family:'Roboto Condensed',Arial,sans-serif;color:var(--navy);font-size:14.5px">PROFESSIONAL CLEANING SERVICES</h2>
    <div class="abs" style="top:452px;width:100%;text-align:center;color:var(--sky);font-size:11px">“We Enjoy Doing the Dirty Work”</div>
    <div class="phone-btn" style="left:26px;top:477px;width:180px">
      <svg viewBox="0 0 16 16"><circle cx="8" cy="8" r="7" fill="none" stroke="#fff" stroke-width="1.4"/><path d="M5.5 4.5l1.5 1.6-.7 1c.5 1 1.3 1.8 2.3 2.3l1-.7 1.6 1.5-.9 1.1C8.4 11 5 7.6 4.4 5.4z" fill="#fff"/></svg>(302) 555-0148</div>
  </div>
</section>

<!-- Inside spread -->
<section class="sheet sheet--inside">

  <!-- Priority panel -->
  <div class="panel navy-bg" style="left:0;width:221px">
    <div class="photo" role="img" aria-label="Photo of a gloved cleaner wiping a conference table lined with microphones" style="left:0;top:0;width:221px;height:225px;background:linear-gradient(160deg,#c9b08e 0%,#8e7a62 45%,#3f3a36 100%)"></div>
    <svg class="abs" style="left:0;top:195px" width="221" height="50" viewBox="0 0 221 50" preserveAspectRatio="none">
      <path d="M0 32 Q110 -2 221 20 L221 50 L0 50Z" fill="var(--navy)"/>
      <path d="M0 26 Q110 -8 221 14 L221 22 Q110 0 0 34Z" fill="#fff"/>
      <path d="M0 22 Q110 -12 221 10 L221 14 Q110 -8 0 26Z" fill="var(--green)"/>
    </svg>
    <h3 class="abs" style="top:255px;left:10px;color:var(--green);font-size:13.5px;font-weight:600">Your Business Is Our #1 Priority</h3>
    <p class="abs" style="top:277px;left:12px;width:200px;color:#fff;font-size:8.7px;line-height:11px;text-align:justify">A clean, organized environment helps businesses run smoothly. The professional team at Clear Meadow Cleaning Services offers great value, exceptional commercial cleaning services in and focuses on providing the quality cleaning that your business deserves. Knowing that every office or facility has individual needs, Clear Meadow Cleaning Services will customize commercial cleaning services for businesses and offices.</p>
    <p class="abs" style="top:391px;left:12px;width:200px;color:#fff;font-size:8.7px;line-height:11px;text-align:justify">We can accommodate many types of commercial cleaning jobs, and we are fully equipped to handle the special needs of your facility.</p>
    <p class="abs" style="top:443px;left:12px;width:200px;color:var(--sky);font-size:9.2px;line-height:12px;text-align:center">Call Clear Meadow Cleaning Services today for a free commercial cleaning quote!</p>
    <div class="phone-btn" style="left:20px;top:470px;width:180px">
      <svg viewBox="0 0 16 16"><circle cx="8" cy="8" r="7" fill="none" stroke="#fff" stroke-width="1.4"/><path d="M5.5 4.5l1.5 1.6-.7 1c.5 1 1.3 1.8 2.3 2.3l1-.7 1.6 1.5-.9 1.1C8.4 11 5 7.6 4.4 5.4z" fill="#fff"/></svg>(302) 555-0148</div>
    <div class="abs" style="top:501px;width:100%;text-align:center;color:#fff;font-size:10.5px">www.quentin-v.sitenook.example</div>
  </div>

  <!-- Offer panel -->
  <div class="panel" style="left:221px;width:222px;background:linear-gradient(90deg,#f4f4f4,#fff 20%,#fff 80%,#ededed)">
    <div class="abs brand-mark" style="left:0;top:22px;width:222px;flex-direction:column">
      <span class="brand-name">Clear Meadow<br>Cleaning Services</span>
      <span class="brand-dot" style="width:30px;height:30px"></span>
    </div>
    <div class="abs tagline" style="top:111px">We Enjoy Doing The Dirty work</div>
    <p class="abs" style="top:135px;left:12px;width:199px;font-size:8.6px;line-height:11px;color:var(--muted);text-align:justify">Whether you're looking for daily, weekly, bi-weekly or monthly cleaning for commercial properties, Clear Meadow Cleaning Services will customize a schedule that works best for your customers and your employees.</p>
    <ul class="abs offer-list" style="top:197px;left:13px">
      <li>Office Cleaning</li><li>Janitorial Services</li><li>Floor Stripping &amp; Waxing</li><li>Day Porter Services</li><li>Window Cleaning</li><li>Kitchen Cleaning</li><li>Restroom Cleaning</li><li>Construction Clean-up</li><li>Deep Cleaning</li><li>Vacant Buildings</li><li>And more!</li>
    </ul>
    <div class="abs" style="top:404px;width:100%;text-align:center;color:var(--sky);font-size:11px">“We Enjoy Doing the Dirty Work”</div>
    <div class="photo" role="img" aria-label="Round photo of gloves and a sponge" style="left:18px;top:425px;width:58px;height:58px;border-radius:50%;border:2px solid #fff;box-shadow:0 1px 4px rgba(0,0,0,.3);background:radial-gradient(circle,#f2d7e6,#b9c6d3)"></div>
    <div class="photo" role="img" aria-label="Round photo of a bucket of cleaning supplies" style="left:82px;top:421px;width:62px;height:62px;border-radius:50%;border:2px solid #fff;box-shadow:0 1px 4px rgba(0,0,0,.3);background:radial-gradient(circle,#f5e06a,#3aa3dc)"></div>
    <div class="photo" role="img" aria-label="Round photo of an upright vacuum cleaner" style="left:148px;top:425px;width:58px;height:58px;border-radius:50%;border:2px solid #fff;box-shadow:0 1px 4px rgba(0,0,0,.3);background:radial-gradient(circle,#e3e6e8,#9aa3aa)"></div>
  </div>

  <!-- Why choose panel -->
  <div class="panel" style="left:443px;width:223px">
    <div class="abs navy-bg" style="left:0;top:0;width:223px;height:345px"></div>
    <h3 class="abs" style="top:28px;left:10px;color:var(--green);font-size:13.5px;font-weight:600">WHY CHOOSE US?</h3>
    <ul class="abs checklist" style="top:45px;left:10px;width:200px">
      <li><span class="tick"></span>Always have a personal point of contact.</li>
      <li><span class="tick"></span>Full on-site service management.</li>
      <li><span class="tick"></span>Bespoke service suited to your requirements.</li>
      <li><span class="tick"></span>Ethical employers.</li>
      <li><span class="tick"></span>Over 2+ years of satisfied customers.</li>
      <li><span class="tick"></span>Free No Obligation Quote.</li>
      <li><span class="tick"></span>Security Of A Fully Bonded Company.</li>
      <li><span class="tick"></span>100% Satisfaction Guarantee On All Service.</li>
      <li style="border-bottom:none"><span class="tick"></span>A Fully Insured Company.</li>
    </ul>
    <svg class="abs" style="left:80px;top:265px" width="64" height="13" viewBox="0 0 64 13">
      <g fill="#f5c542">
        <path id="star" d="M6.5 0l1.9 4.1 4.5.5-3.4 3 1 4.4-4-2.3-4 2.3 1-4.4-3.4-3 4.5-.5z"/>
        <use href="#star" x="13"/><use href="#star" x="26"/><use href="#star" x="39"/><use href="#star" x="52"/>
      </g>
    </svg>
    <p class="abs" style="top:282px;left:10px;width:203px;text-align:center;color:#fff;font-size:7.8px;line-height:10px;font-style:italic">Clear Meadow Cleaning Services cleans our business as well as our home. Always a great job. Great and friendly service all the time. I recommend Clear Meadow to everyone.</p>
    <div class="photo" role="img" aria-label="Photo of a wet floor being mopped beside a yellow caution sign" style="left:0;top:335px;width:223px;height:182px;background:linear-gradient(180deg,#7c8c88 0%,#4f5e5c 60%,#2f3838 100%)"></div>
    <svg class="abs" style="left:0;top:318px" width="223" height="45" viewBox="0 0 223 45" preserveAspectRatio="none">
      <path d="M0 12 Q110 40 223 4 L223 0 L0 0Z" fill="var(--navy-deep)"/>
      <path d="M0 12 Q110 40 223 4 L223 12 Q110 48 0 20Z" fill="#fff"/>
      <path d="M0 20 Q110 48 223 12 L223 18 Q110 54 0 26Z" fill="var(--green)"/>
    </svg>
  </div>
</section>

</body>
</html>
```